Prickly Heat Powder

prickly heat powders are used in summers to provide cooling effect to body and relief body from heat effects during summers.

we have 4 variants of prickly heat.

1) Menthol
2) Rose
3) Lemon
4) Neem

Bottle is in round cylinder shape. It also has a cap. Will share pictures of bottle and cap tomorrow.

Brand Name is KAVELO.

Total label size will be 180mm width * 140mm height. But main design will be small because bottle is round.

Target Market(s)

B Class.
C plus and C.
Masses

Industry/Entity Type

Cosmetics

Requirements
Must have
• icy effect, joyful and playful
Nice to have
• joyful and eye catching designs. more colors would be good.
• Polar bear might look nice.
• Kavelo Logo to be bold and prominent.

```html
<!DOCTYPE html>
<html lang="en">
<head>
<meta charset="utf-8">
<title>Kavelo Prickly Heat Powder – Label Range</title>
<link rel="stylesheet" href="https://fonts.googleapis.com/css2?family=Titillium+Web:ital,wght@0,700;0,900;1,700&display=swap">
<style>
  :root {
    --page-top: #ffffff;
    --page-bottom: #dcdcdc;
    --band-blue-dark: #1f2f8f;
    --band-blue: #2f47b8;
    --band-blue-light: #4a63d0;
    --silver-dark: #8e9296;
    --silver-light: #f2f3f4;
    --ink-white: #ffffff;
    --ice-light: #e3eef5;
    --ice-mid: #b4cadb;
    --ice-deep: #8fadc4;
    --neem: #3a9a5c;
    --neem-light: #5cc07c;
    --neem-art: #3f9a2e;
    --menthol: #1fb2da;
    --menthol-light: #6fd3ee;
    --menthol-art: #46c25a;
    --rose: #d9437f;
    --rose-light: #f07aa8;
    --rose-art: #e0407e;
    --lemon: #e7c331;
    --lemon-light: #f4dc6a;
    --lemon-art: #f2c01c;
  }
  html, body {
    margin: 0;
    width: 1200px;
    height: 920px;
    overflow: hidden;
  }
  body {
    background: linear-gradient(to bottom, var(--page-top), var(--page-bottom));
    font-family: "Titillium Web", Arial, sans-serif;
  }
  .label-range {
    position: absolute;
    left: 125px;
    top: 230px;
    display: flex;
    gap: 50px;
  }
  .label {
    position: relative;
    width: 200px;
    height: 460px;
  }
  .label--neem { --tone: var(--neem); --tone-light: var(--neem-light); --art: var(--neem-art); }
  .label--menthol { --tone: var(--menthol); --tone-light: var(--menthol-light); --art: var(--menthol-art); }
  .label--rose { --tone: var(--rose); --tone-light: var(--rose-light); --art: var(--rose-art); }
  .label--lemon { --tone: var(--lemon); --tone-light: var(--lemon-light); --art: var(--lemon-art); }
  .label svg { position: absolute; inset: 0; display: block; }
  .stop-tone { stop-color: var(--tone); }
  .stop-tone-light { stop-color: var(--tone-light); }
  .stop-art { stop-color: var(--art); }
  .stop-ice { stop-color: var(--ice-light); }
  .stop-ice-mid { stop-color: var(--ice-mid); }
  .stop-ice-deep { stop-color: var(--ice-deep); }
  .stop-silver-light { stop-color: var(--silver-light); }
  .stop-silver-dark { stop-color: var(--silver-dark); }
  .stop-blue-dark { stop-color: var(--band-blue-dark); }
  .stop-blue { stop-color: var(--band-blue); }
  .stop-blue-light { stop-color: var(--band-blue-light); }
  .product-type {
    position: absolute;
    left: 44px;
    top: 40px;
    margin: 0;
    color: var(--ink-white);
    font-style: italic;
    font-weight: 700;
    font-size: 17px;
    line-height: 15px;
    text-transform: uppercase;
    transform: rotate(-14deg);
    transform-origin: left top;
  }
  .brand-name {
    position: absolute;
    left: 0;
    width: 200px;
    top: 132px;
    margin: 0;
    text-align: center;
    color: var(--ink-white);
    font-weight: 900;
    font-size: 44px;
    line-height: 50px;
    letter-spacing: 1px;
    transform: rotate(-20deg);
  }
  .variant-name {
    position: absolute;
    left: 40px;
    width: 160px;
    top: 398px;
    margin: 0;
    text-align: center;
    color: var(--ink-white);
    font-weight: 700;
    font-size: 22px;
    line-height: 26px;
    text-transform: uppercase;
    transform: rotate(-11deg);
  }
</style>
</head>
<body>
<main class="label-range">

  <section class="label label--neem">
    <svg viewBox="0 0 200 460" width="200" height="460">
      <defs>
        <radialGradient id="neem-art" cx="0.48" cy="0.68" r="0.7">
          <stop offset="0" class="stop-art"/><stop offset="0.22" class="stop-art"/><stop offset="0.4" class="stop-ice-deep"/><stop offset="0.65" class="stop-ice-mid"/><stop offset="0.85" class="stop-ice"/><stop offset="1" class="stop-tone-light"/>
        </radialGradient>
        <linearGradient id="neem-base" x1="0" y1="0" x2="1" y2="0"><stop offset="0" class="stop-tone-light"/><stop offset="1" class="stop-tone"/></linearGradient>
        <linearGradient id="neem-silver" x1="0" y1="0" x2="1" y2="0"><stop offset="0" class="stop-silver-dark"/><stop offset="0.5" class="stop-silver-light"/><stop offset="1" class="stop-silver-dark"/></linearGradient>
        <linearGradient id="neem-blue" x1="0" y1="0" x2="1" y2="0"><stop offset="0" class="stop-blue-dark"/><stop offset="0.5" class="stop-blue-light"/><stop offset="1" class="stop-blue"/></linearGradient>
      </defs>
      <rect class="label-base" width="200" height="460" fill="url(#neem-base)"/>
      <path class="hero-visual" role="img" aria-label="Crushed ice cubes with neem leaves and blossoms on a cool splash" d="M0,225 Q100,190 200,150 L200,380 Q100,408 0,420 Z" fill="url(#neem-art)"/>
      <path class="silver-edge" d="M0,152 Q100,112 200,77 L200,90 Q100,125 0,165 Z" fill="url(#neem-silver)"/>
      <path class="brand-band" d="M0,165 Q100,125 200,90 L200,150 Q100,190 0,225 Z" fill="url(#neem-blue)"/>
      <path class="silver-edge" d="M0,225 Q100,190 200,150 L200,160 Q100,199 0,234 Z" fill="url(#neem-silver)"/>
      <path class="silver-edge" d="M0,410 Q100,398 200,370 L200,380 Q100,408 0,420 Z" fill="url(#neem-silver)"/>
      <path class="variant-band" d="M0,420 Q100,408 200,380 L200,425 Q100,440 0,448 Z" fill="url(#neem-blue)"/>
      <path class="silver-edge" d="M0,448 Q100,440 200,425 L200,432 Q100,446 0,454 Z" fill="url(#neem-silver)"/>
    </svg>
    <p class="product-type">Prickly<br>Heat<br>Powder</p>
    <h2 class="brand-name">KAVELO</h2>
    <p class="variant-name">Neem</p>
  </section>

  <section class="label label--menthol">
    <svg viewBox="0 0 200 460" width="200" height="460">
      <defs>
        <radialGradient id="menthol-art" cx="0.48" cy="0.68" r="0.7">
          <stop offset="0" class="stop-art"/><stop offset="0.22" class="stop-art"/><stop offset="0.4" class="stop-ice-deep"/><stop offset="0.65" class="stop-ice-mid"/><stop offset="0.85" class="stop-ice"/><stop offset="1" class="stop-tone-light"/>
        </radialGradient>
        <linearGradient id="menthol-base" x1="0" y1="0" x2="1" y2="0"><stop offset="0" class="stop-tone-light"/><stop offset="1" class="stop-tone"/></linearGradient>
        <linearGradient id="menthol-silver" x1="0" y1="0" x2="1" y2="0"><stop offset="0" class="stop-silver-dark"/><stop offset="0.5" class="stop-silver-light"/><stop offset="1" class="stop-silver-dark"/></linearGradient>
        <linearGradient id="menthol-blue" x1="0" y1="0" x2="1" y2="0"><stop offset="0" class="stop-blue-dark"/><stop offset="0.5" class="stop-blue-light"/><stop offset="1" class="stop-blue"/></linearGradient>
      </defs>
      <rect class="label-base" width="200" height="460" fill="url(#menthol-base)"/>
      <path class="hero-visual" role="img" aria-label="Crushed ice cubes with fresh mint leaves in a water splash" d="M0,225 Q100,190 200,150 L200,380 Q100,408 0,420 Z" fill="url(#menthol-art)"/>
      <path class="silver-edge" d="M0,152 Q100,112 200,77 L200,90 Q100,125 0,165 Z" fill="url(#menthol-silver)"/>
      <path class="brand-band" d="M0,165 Q100,125 200,90 L200,150 Q100,190 0,225 Z" fill="url(#menthol-blue)"/>
      <path class="silver-edge" d="M0,225 Q100,190 200,150 L200,160 Q100,199 0,234 Z" fill="url(#menthol-silver)"/>
      <path class="silver-edge" d="M0,410 Q100,398 200,370 L200,380 Q100,408 0,420 Z" fill="url(#menthol-silver)"/>
      <path class="variant-band" d="M0,420 Q100,408 200,380 L200,425 Q100,440 0,448 Z" fill="url(#menthol-blue)"/>
      <path class="silver-edge" d="M0,448 Q100,440 200,425 L200,432 Q100,446 0,454 Z" fill="url(#menthol-silver)"/>
    </svg>
    <p class="product-type">Prickly<br>Heat<br>Powder</p>
    <h2 class="brand-name">KAVELO</h2>
    <p class="variant-name">Menthol</p>
  </section>

  <section class="label label--rose">
    <svg viewBox="0 0 200 460" width="200" height="460">
      <defs>
        <radialGradient id="rose-art" cx="0.55" cy="0.7" r="0.7">
          <stop offset="0" class="stop-art"/><stop offset="0.22" class="stop-art"/><stop offset="0.4" class="stop-ice-deep"/><stop offset="0.65" class="stop-ice-mid"/><stop offset="0.85" class="stop-ice"/><stop offset="1" class="stop-tone-light"/>
        </radialGradient>
        <linearGradient id="rose-base" x1="0" y1="0" x2="1" y2="0"><stop offset="0" class="stop-tone-light"/><stop offset="1" class="stop-tone"/></linearGradient>
        <linearGradient id="rose-silver" x1="0" y1="0" x2="1" y2="0"><stop offset="0" class="stop-silver-dark"/><stop offset="0.5" class="stop-silver-light"/><stop offset="1" class="stop-silver-dark"/></linearGradient>
        <linearGradient id="rose-blue" x1="0" y1="0" x2="1" y2="0"><stop offset="0" class="stop-blue-dark"/><stop offset="0.5" class="stop-blue-light"/><stop offset="1" class="stop-blue"/></linearGradient>
      </defs>
      <rect class="label-base" width="200" height="460" fill="url(#rose-base)"/>
      <path class="hero-visual" role="img" aria-label="Crushed ice cubes with a pink rose bloom and bud" d="M0,225 Q100,190 200,150 L200,380 Q100,408 0,420 Z" fill="url(#rose-art)"/>
      <path class="silver-edge" d="M0,152 Q100,112 200,77 L200,90 Q100,125 0,165 Z" fill="url(#rose-silver)"/>
      <path class="brand-band" d="M0,165 Q100,125 200,90 L200,150 Q100,190 0,225 Z" fill="url(#rose-blue)"/>
      <path class="silver-edge" d="M0,225 Q100,190 200,150 L200,160 Q100,199 0,234 Z" fill="url(#rose-silver)"/>
      <path class="silver-edge" d="M0,410 Q100,398 200,370 L200,380 Q100,408 0,420 Z" fill="url(#rose-silver)"/>
      <path class="variant-band" d="M0,420 Q100,408 200,380 L200,425 Q100,440 0,448 Z" fill="url(#rose-blue)"/>
      <path class="silver-edge" d="M0,448 Q100,440 200,425 L200,432 Q100,446 0,454 Z" fill="url(#rose-silver)"/>
    </svg>
    <p class="product-type">Prickly<br>Heat<br>Powder</p>
    <h2 class="brand-name">KAVELO</h2>
    <p class="variant-name">Rose</p>
  </section>

  <section class="label label--lemon">
    <svg viewBox="0 0 200 460" width="200" height="460">
      <defs>
        <radialGradient id="lemon-art" cx="0.55" cy="0.68" r="0.7">
          <stop offset="0" class="stop-art"/><stop offset="0.22" class="stop-art"/><stop offset="0.4" class="stop-ice-deep"/><stop offset="0.65" class="stop-ice-mid"/><stop offset="0.85" class="stop-ice"/><stop offset="1" class="stop-tone-light"/>
        </radialGradient>
        <linearGradient id="lemon-base" x1="0" y1="0" x2="1" y2="0"><stop offset="0" class="stop-tone-light"/><stop offset="1" class="stop-tone"/></linearGradient>
        <linearGradient id="lemon-silver" x1="0" y1="0" x2="1" y2="0"><stop offset="0" class="stop-silver-dark"/><stop offset="0.5" class="stop-silver-light"/><stop offset="1" class="stop-silver-dark"/></linearGradient>
        <linearGradient id="lemon-blue" x1="0" y1="0" x2="1" y2="0"><stop offset="0" class="stop-blue-dark"/><stop offset="0.5" class="stop-blue-light"/><stop offset="1" class="stop-blue"/></linearGradient>
      </defs>
      <rect class="label-base" width="200" height="460" fill="url(#lemon-base)"/>
      <path class="hero-visual" role="img" aria-label="Crushed ice cubes with a whole lemon and a lemon half" d="M0,225 Q100,190 200,150 L200,380 Q100,408 0,420 Z" fill="url(#lemon-art)"/>
      <path class="silver-edge" d="M0,152 Q100,112 200,77 L200,90 Q100,125 0,165 Z" fill="url(#lemon-silver)"/>
      <path class="brand-band" d="M0,165 Q100,125 200,90 L200,150 Q100,190 0,225 Z" fill="url(#lemon-blue)"/>
      <path class="silver-edge" d="M0,225 Q100,190 200,150 L200,160 Q100,199 0,234 Z" fill="url(#lemon-silver)"/>
      <path class="silver-edge" d="M0,410 Q100,398 200,370 L200,380 Q100,408 0,420 Z" fill="url(#lemon-silver)"/>
      <path class="variant-band" d="M0,420 Q100,408 200,380 L200,425 Q100,440 0,448 Z" fill="url(#lemon-blue)"/>
      <path class="silver-edge" d="M0,448 Q100,440 200,425 L200,432 Q100,446 0,454 Z" fill="url(#lemon-silver)"/>
    </svg>
    <p class="product-type">Prickly<br>Heat<br>Powder</p>
    <h2 class="brand-name">KAVELO</h2>
    <p class="variant-name">Lemon</p>
  </section>

</main>
</body>
</html>
```